Business Cards, Letter Heads and a4 size envolpes
Brantwick Holdings
Business Cards, Letter Heads and a4 size envolpes - Financial Services
Creative Brief
Simple
Jad K. Lorenby
Managing Partner
T : +971 4 3867041 M : +971 50 6183024(Ae) M: +255 773 482615 (Tz) P.O. Box 6174 Dubai UAE
jad@brantwickholdings-example.com
www.brantwickholdings-example.com

```html
<!DOCTYPE html>
<html lang="en">
<head>
<meta charset="utf-8">
<title>Brantwick Holdings — Business Cards</title>
<link rel="stylesheet" href="https://fonts.googleapis.com/css2?family=Jost:wght@300;400&display=swap">
<style>
  :root {
    --backdrop: #d6d6d6;
    --card: #0b0b0b;
    --ink: #f2f2f2;
    --ink-soft: #b9b9b9;
    --ink-dim: #8a8a8a;
  }
  * { margin: 0; padding: 0; box-sizing: border-box; }
  html, body {
    width: 1200px; height: 901px; overflow: hidden;
    background: var(--backdrop);
    font-family: "Jost", "Futura", sans-serif;
    font-weight: 300;
  }
  .stage { position: relative; width: 1200px; height: 901px; }
  .card {
    position: absolute;
    width: 620px; height: 354px;
    background: var(--card);
    border-radius: 3px;
    box-shadow: 0 10px 28px rgba(0,0,0,0.28);
    color: var(--ink);
  }
  .card--back { left: 150px; top: 62px; }
  .card--front { left: 430px; top: 478px; }

  .brand {
    position: absolute; left: 0; right: 0;
    display: flex; flex-direction: column; align-items: center; gap: 10px;
  }
  .card--back .brand { top: 118px; }
  .card--front .brand { top: 42px; }
  .brand-square {
    width: 26px; height: 26px;
    border: 1.5px solid var(--ink);
  }
  .brand-name {
    font-size: 21px; font-weight: 300; letter-spacing: 1px;
    color: var(--ink);
  }
  .back-web {
    position: absolute; left: 0; right: 0; bottom: 46px;
    text-align: center; font-size: 12px; letter-spacing: 1px;
    color: var(--ink-dim);
  }
  .person { position: absolute; left: 44px; top: 150px; }
  .person-name { font-size: 18px; font-weight: 400; letter-spacing: 0.5px; }
  .person-role { font-size: 12px; color: var(--ink-soft); margin-top: 4px; }
  .contact {
    position: absolute; left: 360px; bottom: 30px;
    font-size: 11.5px; line-height: 1.55; color: var(--ink-soft);
    list-style: none;
  }
  .contact .gap { margin-top: 10px; }
</style>
</head>
<body>
<main class="stage">
  <section class="card card--back" aria-label="Business card back">
    <div class="brand">
      <span class="brand-square"></span>
      <span class="brand-name">Brantwick Holdings</span>
    </div>
    <p class="back-web">www.brantwickholdings-example.com</p>
  </section>

  <section class="card card--front" aria-label="Business card front">
    <div class="brand">
      <span class="brand-square"></span>
      <span class="brand-name">Brantwick Holdings</span>
    </div>
    <div class="person">
      <p class="person-name">Jad K. Lorenby</p>
      <p class="person-role">Managing Partner</p>
    </div>
    <ul class="contact">
      <li>P.O. Box 6174, Dubai , UAE</li>
      <li class="gap">T : +971 4 3867041</li>
      <li>M : +971 50 6183024(Ae)</li>
      <li>M: +255 773 482615 (Tz)</li>
      <li class="gap">jad@brantwickholdings-example.com</li>
      <li>www.brantwickholdings-example.com</li>
    </ul>
  </section>
</main>
</body>
</html>
```